Wordpress template re-design of current website

We need a WordPress template design and new look for our existing website. Our existing site it located at www.velmoro.com.au We are a tech company and want a fresh, clean modern website that matches our brand, services and logo colors. Our main Services are hospitality solutions, Velmoro TV solution and managed networks, more information on these can come from our existing website.

Target Market(s)

We are a tech company so must have a modern feel for new technology

Industry/Entity Type

It Company

Number of Pages Required

5+ page

Font styles to use
Sans Serif

Requirements
Must have
• Be based on a wordpress templete design and match the services that we have in our existing website, in the testimonials want a place for video testimonials as well as text. Nice clean icons used for graphics to represent services.
Nice to have
• nice visual representation of our services in the way of clean icons etc
Should not have
• Clutter

```html
<!DOCTYPE html>
<html lang="en">
<head>
<meta charset="utf-8">
<title>Velmoro Wireless</title>
<link href="https://fonts.googleapis.com/css2?family=Exo+2:ital,wght@0,600;0,700;1,700&family=Lato:wght@400;700&family=Oswald:wght@500&display=swap" rel="stylesheet">
<style>
:root{
  --navy:#0d3b7f;
  --blue:#1b5cab;
  --btn:#1f4f8e;
  --sky:#dbe7f7;
  --grey-bg:#eeeeee;
  --text:#555;
  --dark:#333;
  --footer:#2e2e2e;
  --footer-bar:#1f1f1f;
  --icon:#5b6b7c;
}
*{box-sizing:border-box;margin:0;padding:0}
html,body{width:1200px;height:3255px;overflow:hidden}
body{position:relative;font-family:'Lato',sans-serif;color:var(--text);background:#fff;font-size:13px}
.abs{position:absolute}
.heading{font-family:'Exo 2',sans-serif;font-style:italic;font-weight:700;color:var(--navy);font-size:27px;text-align:center}
.heading-wrap{position:absolute;left:0;width:1200px;text-align:center}
.heading-wrap .heading{display:inline-block;padding:0 22px;position:relative}
.heading-wrap .heading::before,.heading-wrap .heading::after{content:"";position:absolute;top:50%;width:46px;border-top:2px dotted #b9c6d8}
.heading-wrap .heading::before{right:100%}
.heading-wrap .heading::after{left:100%}
.btn{position:absolute;background:var(--btn);color:#fff;font-family:'Oswald',sans-serif;font-size:14px;letter-spacing:.3px;text-align:center;border-bottom:3px solid #0c2f5e}

/* header */
.site-header{position:absolute;left:0;top:0;width:1200px;height:88px;background:#fff;z-index:2}
.topbar{position:absolute;left:330px;top:0;width:870px;height:34px;background:#e9ecef}
.topbar span{position:absolute;top:9px;font-size:13px;color:#555;white-space:nowrap}
.social-sq{position:absolute;top:6px;width:21px;height:21px;background:var(--blue)}
.brand{position:absolute;left:86px;top:18px;display:flex;align-items:center;gap:10px}
.brand-name{font-family:'Exo 2',sans-serif;font-weight:700;font-size:34px;color:var(--navy)}
.brand-dot{width:34px;height:34px;border-radius:50%;background:var(--blue)}
.nav a{position:absolute;top:37px;height:43px;line-height:43px;font-size:14px;color:#444;text-decoration:none;text-align:center}
.nav .active{background:var(--sky);color:var(--blue)}
.nav .portal{background:var(--navy);color:#fff;font-weight:700}

/* hero */
.hero{position:absolute;left:0;top:88px;width:1200px;height:546px;background:linear-gradient(120deg,#3a2a1e 0%,#7a5a3c 35%,#b79776 55%,#6d5a48 75%,#2e2620 100%)}
.hero-title{position:absolute;top:310px;left:0;width:1200px;text-align:center;font-family:'Oswald',sans-serif;font-weight:500;font-size:44px;color:#fff;letter-spacing:-.5px}
.hero-btn{position:absolute;left:508px;top:386px;width:182px;height:46px;line-height:46px;background:#111;color:#fff;font-family:'Oswald',sans-serif;font-size:17px;text-align:center}

/* welcome */
.welcome-text{position:absolute;left:110px;top:752px;width:980px;font-size:13px;line-height:27px;text-align:center;color:#666}

/* band */
.band{position:absolute;left:0;top:976px;width:1200px;height:168px;background:linear-gradient(180deg,#1c5aa6,#134a8e)}
.band p{position:absolute;top:34px;left:60px;width:1080px;text-align:center;color:#fff;font-family:'Exo 2',sans-serif;font-weight:700;font-size:27px;line-height:46px}

/* services */
.service{position:absolute;top:1269px;width:258px;height:272px;text-align:center}
.service.is-active{background:#e4edfa;border:2px solid #b5cbec;clip-path:polygon(0 0,84% 0,100% 14%,100% 100%,16% 100%,0 86%)}
.service svg{display:block;margin:14px auto 0}
.service h3{font-size:19px;font-weight:700;color:#222;margin-top:18px}
.service.is-active h3{color:var(--navy)}
.service p{font-size:13px;line-height:24px;color:#666;margin-top:6px;padding:0 34px}
.service .more{font-size:12px;font-weight:700;color:#222;margin-top:6px}

/* work */
.work{position:absolute;left:0;top:1584px;width:1200px;height:710px;background:var(--grey-bg)}
.filters{position:absolute;top:1711px;left:0;width:1200px;text-align:center;font-size:13px;color:#555}
.filters span{display:inline-block;padding:3px 10px;margin:0 2px}
.filters .on{background:#fff;border:1px solid #ddd}
.tile{position:absolute}
.tile.cut-tl{clip-path:polygon(22px 0,100% 0,100% 100%,0 100%,0 22px)}
.tile.cut-tr{clip-path:polygon(0 0,calc(100% - 22px) 0,100% 22px,100% 100%,0 100%)}
.tile.cut-bl{clip-path:polygon(0 0,100% 0,100% 100%,22px 100%,0 calc(100% - 22px))}
.tile.cut-br{clip-path:polygon(0 0,100% 0,100% calc(100% - 22px),calc(100% - 22px) 100%,0 100%)}
.feature-tile{position:absolute;left:417px;top:1758px;width:358px;height:423px;background:#ffffff}
.feature-inner{position:absolute;left:12px;top:12px;right:12px;bottom:0;background:linear-gradient(180deg,#2b5fb0,#1b4c96)}
.feature-inner h4{position:absolute;top:148px;width:100%;text-align:center;color:#fff;font-family:'Oswald',sans-serif;font-weight:500;font-size:20px;line-height:30px}

/* clients & inquiry */
.clients-text{position:absolute;left:87px;top:2420px;width:500px;font-size:13px;line-height:23px;color:#555}
.client-box{position:absolute;top:2513px;width:150px;height:70px;border:1px solid #ddd;background:#fff;display:flex;align-items:center;justify-content:center;font-weight:700;font-size:16px;color:var(--navy)}
.field{position:absolute;border:1px solid #ccc;background:#f7f7f7;font-size:11px;color:#666;padding:9px 10px}

/* testimonials */
.testimonials{position:absolute;left:87px;top:2637px;width:1026px;height:277px;background:linear-gradient(180deg,#6a7684,#55616f)}
.quote{position:absolute;left:286px;top:130px;width:600px;color:#fff;font-size:13px;line-height:20px}
.avatar{position:absolute;left:199px;top:123px;width:72px;height:72px;border-radius:50%;background:#c9ced4;border:3px solid #fff}
.arrow{position:absolute;top:132px;color:#fff;font-size:26px}

/* footer */
.site-footer{position:absolute;left:0;top:2914px;width:1200px;height:286px;background:var(--footer);color:#ccc}
.fcol{position:absolute;top:72px}
.fcol h5{font-size:15px;font-weight:700;color:#fff;padding-bottom:8px;border-bottom:1px dotted #777;margin-bottom:12px}
.fcol li{list-style:none;font-size:12px;line-height:24px;color:#ccc}
.fcol li::before{content:"› ";color:#aaa}
.social-mark{display:inline-block;width:18px;height:18px;background:#fff;vertical-align:middle;margin-right:8px}
.footer-bar{position:absolute;left:0;top:3200px;width:1200px;height:55px;background:var(--footer-bar);color:#bbb;font-size:12px}
</style>
</head>
<body>

<header class="site-header">
  <div class="brand"><span class="brand-dot"></span><span class="brand-name">Velmoro</span></div>
  <div class="topbar">
    <span style="left:340px">✉ sales@velmoro.com.au</span>
    <span style="left:530px">☏ (123) 456 7890</span>
    <div class="social-sq" style="left:690px"></div>
    <div class="social-sq" style="left:715px"></div>
    <div class="social-sq" style="left:740px"></div>
    <div class="social-sq" style="left:765px"></div>
  </div>
  <nav class="nav">
    <a class="active" style="left:500px;width:86px">Home</a>
    <a style="left:596px;width:76px">About</a>
    <a style="left:690px;width:86px">Services</a>
    <a style="left:794px;width:100px">Our Work</a>
    <a style="left:910px;width:90px">Contact</a>
    <a class="portal" style="left:1005px;width:108px">PORTAL</a>
  </nav>
</header>

<section class="hero" role="img" aria-label="Hotel lobby with reception desk and staff"></section>
<h1 class="hero-title">BEST HOSPITALITY SOLUTION</h1>
<div class="hero-btn">CONTACT NOW !</div>

<div class="heading-wrap" style="top:680px"><h2 class="heading">Well Come To Velmoro Wireless</h2></div>
<p class="welcome-text">Velmoro Wireless is at the forefront of revolutionising high-speed internet access (HSIA) services. We offer complete wireless solutions: Right from developing individual components such as hotspots and access controllers, to installation of the internet infrastructure. Once we setup the HSIA for our clients, we back it up with round-the-clock tech support. Velmoro's expertise in wireless technology has attracted a growing client base from all over Australia.In 2002, our tech experts developed a user-friendly, feature-rich software platform. Today, we deliver customised information systems based on the platform. Our robust, secure network requires minimal maintenance and can be monitored remotely from anywhere in the world.</p>
<div class="btn" style="left:550px;top:886px;width:98px;height:34px;line-height:31px">READ MORE</div>

<section class="band" role="img" aria-label="Blue band over a faint photo of a business crowd">
  <p>We Strive To Out Work Our Competition With An Effective Approach And A Powerful Skill Set, Which Is Why Were Industry Leading.</p>
</section>

<div class="heading-wrap" style="top:1194px"><h2 class="heading">Our Awesome Services</h2></div>

<div class="service" style="left:79px">
  <svg width="130" height="130" viewBox="0 0 130 130"><circle cx="65" cy="65" r="62" fill="none" stroke="#c5ccd4" stroke-width="3" stroke-dasharray="2 5"/><circle cx="65" cy="65" r="56" fill="var(--icon)"/><circle cx="65" cy="65" r="50" fill="none" stroke="#fff" stroke-width="4"/><path d="M42 62l23-18 23 18M47 58v24h36V58M52 74h26M52 70h8" fill="none" stroke="#fff" stroke-width="4"/></svg>
  <h3>Hospitality</h3><p>Get On The Fastest, Most Flexible Internet Access System</p><div class="more">READ MORE</div>
</div>
<div class="service is-active" style="left:341px">
  <svg width="130" height="130" viewBox="0 0 130 130"><circle cx="65" cy="65" r="62" fill="none" stroke="#c5ccd4" stroke-width="3" stroke-dasharray="2 5"/><circle cx="65" cy="65" r="56" fill="var(--navy)"/><circle cx="65" cy="65" r="50" fill="none" stroke="#fff" stroke-width="4"/><rect x="52" y="40" width="26" height="48" rx="4" fill="none" stroke="#fff" stroke-width="4"/><circle cx="65" cy="81" r="2.5" fill="#fff"/></svg>
  <h3>Mobile Solutions</h3><p>Anytime Anywhere Mobile Gateways</p><div class="more" style="color:var(--navy)">READ MORE</div>
</div>
<div class="service" style="left:600px">
  <svg width="130" height="130" viewBox="0 0 130 130"><circle cx="65" cy="65" r="62" fill="none" stroke="#c5ccd4" stroke-width="3" stroke-dasharray="2 5"/><circle cx="65" cy="65" r="56" fill="var(--icon)"/><circle cx="65" cy="65" r="50" fill="none" stroke="#fff" stroke-width="4"/><rect x="44" y="50" width="42" height="32" rx="3" fill="none" stroke="#fff" stroke-width="4"/><path d="M56 40l9 10 9-10M56 88h18" fill="none" stroke="#fff" stroke-width="4"/></svg>
  <h3>Velmoro TV</h3><p>The Complete Information System For Hospitality</p><div class="more">READ MORE</div>
</div>
<div class="service" style="left:861px">
  <svg width="130" height="130" viewBox="0 0 130 130"><circle cx="65" cy="65" r="62" fill="none" stroke="#c5ccd4" stroke-width="3" stroke-dasharray="2 5"/><circle cx="65" cy="65" r="56" fill="var(--icon)"/><circle cx="65" cy="65" r="50" fill="none" stroke="#fff" stroke-width="4"/><path d="M60 56a10 10 0 0 1 10 10M60 46a20 20 0 0 1 20 20" fill="none" stroke="#fff" stroke-width="4"/><circle cx="60" cy="66" r="3" fill="#fff"/><path d="M48 70l8 14h14" fill="none" stroke="#fff" stroke-width="4"/></svg>
  <h3>Social Wi-Fi</h3><p>Maximize Your Business Potential With Social Plugins</p><div class="more">READ MORE</div>
</div>

<section class="work"></section>
<div class="heading-wrap" style="top:1634px"><h2 class="heading">Our Latest Work</h2></div>
<div class="filters"><span class="on">All</span><span>Hospitality</span><span>Mobile Solutions</span><span>Mining and Remote</span><span>Social Wi-Fi</span><span>Velmoro TV</span></div>

<div class="tile cut-tl" role="img" aria-label="Modern apartment tower" style="left:87px;top:1758px;width:317px;height:206px;background:linear-gradient(180deg,#8fb7e0,#c9a88a 70%,#5d6b4a)"></div>
<div class="tile cut-bl" role="img" aria-label="Coach bus on the road" style="left:87px;top:1975px;width:317px;height:206px;background:linear-gradient(180deg,#9dbcd6,#e9e9ea 45%,#9a3b3b 75%,#55574f)"></div>
<div class="feature-tile"><div class="feature-inner" role="img" aria-label="Hospital building with blue overlay">
  <h4>Coastal Hospital<br>Patient Wi-Fi Solution</h4>
  <svg class="abs" style="left:152px;top:216px" width="30" height="30" viewBox="0 0 30 30"><circle cx="15" cy="15" r="14" fill="#fff"/><path d="M15 8v14M8 15h14" stroke="#1b4c96" stroke-width="3"/></svg>
</div></div>
<div class="tile cut-tr" role="img" aria-label="Apartment complex among trees" style="left:796px;top:1758px;width:317px;height:206px;background:linear-gradient(160deg,#3d4a3a,#8f8b7d 50%,#b4b2a8)"></div>
<div class="tile cut-br" role="img" aria-label="Laptop and phone on a desk" style="left:796px;top:1975px;width:317px;height:206px;background:linear-gradient(160deg,#2a1e18,#6e4430 50%,#9a8f86)"></div>
<div class="btn" style="left:552px;top:2203px;width:96px;height:34px;line-height:31px">VIEW MORE</div>

<h2 class="heading abs" style="left:87px;top:2363px;font-size:22px;text-align:left">Our Clients</h2>
<svg class="abs" style="left:538px;top:2367px" width="48" height="22" viewBox="0 0 48 22"><circle cx="11" cy="11" r="9" fill="none" stroke="#888"/><path d="M13 7l-4 4 4 4" fill="none" stroke="#666" stroke-width="2"/><circle cx="36" cy="11" r="9" fill="none" stroke="#888"/><path d="M34 7l4 4-4 4" fill="none" stroke="#666" stroke-width="2"/></svg>
<p class="clients-text">Lorem ipsum dolor sit amet, consectetur adipiscing elit. Vivamus tempus, lacus ut rhoncus malesuada, risus eros rutrum nibh, et fermentum dui tortor sit amet ipsum. Aenean semper tristique velit in cursus.</p>
<div class="client-box" style="left:87px">Harbourline</div>
<div class="client-box" style="left:261px">Tourvana</div>
<div class="client-box" style="left:436px">Mineo</div>

<h2 class="heading abs" style="left:613px;top:2363px;font-size:22px;text-align:left">Touch With Us For Any Inquiry</h2>
<div class="field" style="left:613px;top:2435px;width:162px;height:35px">Name *</div>
<div class="field" style="left:783px;top:2435px;width:162px;height:35px">Email Address *</div>
<div class="field" style="left:953px;top:2435px;width:160px;height:35px">Phone *</div>
<div class="field" style="left:613px;top:2478px;width:500px;height:62px">The message you want to send to me.</div>
<div class="btn" style="left:613px;top:2550px;width:132px;height:33px;line-height:30px">SUBMIT INQUIRY</div>

<section class="testimonials" role="img" aria-label="Faint grid of customer portraits behind the testimonial">
  <div class="heading-wrap" style="left:0;width:1026px;top:48px"><h2 class="heading" style="color:#fff">What Our Customers Say</h2></div>
  <div class="arrow" style="left:78px">‹</div>
  <div class="arrow" style="left:936px">›</div>
  <div class="avatar"></div>
  <p class="quote">❝ Lorem ipsum dolor sit amet, consectetur adipiscing elit. Vivamus tempus, lacus ut rhoncus malesuada, risus eros rutrum nibh, et fermentum dui tortor sit amet ipsum. Aenean semper tristique velit in cursus. Sed sagittis sapien a lectus placerat, eu commodo neque ❞</p>
  <div class="abs" style="left:286px;top:226px;color:#fff;font-size:14px;font-weight:700">Mr. Lorem ipsum <span style="font-weight:400;font-size:12px;margin-left:40px;color:#dde">Today</span> <span style="font-weight:400;font-size:12px;margin-left:40px;color:#dde">▶ Play this Video Testimonial</span></div>
</section>

<footer class="site-footer">
  <div class="fcol" style="left:87px;width:190px"><h5>Quick Links</h5>
    <ul style="float:left;width:95px"><li>Home</li><li>About Us</li><li>Services</li><li>Our Work</li><li>Contact Us</li></ul>
    <ul style="float:left"><li>Portal</li><li>Case Studies</li><li>Testimonials</li><li>News</li><li>Resellers</li></ul>
  </div>
  <div class="fcol" style="left:371px;width:225px"><h5>Newsletter Sign Up</h5>
    <p style="font-size:12px;line-height:18px">Stay updated with latest news from Velmoro Wireless.</p>
    <div style="margin-top:12px;background:#fff;height:32px;color:#777;font-size:12px;line-height:32px;padding-left:12px">✉ Enter your Email</div>
    <div style="margin-top:10px;background:var(--btn);color:#fff;width:84px;height:26px;line-height:26px;text-align:center;font-size:11px;font-weight:700">SUBSCRIBE</div>
  </div>
  <div class="fcol" style="left:688px;width:205px"><h5>Contact Information</h5>
    <p style="font-size:12px;line-height:18px"><b style="color:#fff">Velmoro Wireless</b><br>48 Lakeside Drive Bayview,<br>QLD 4230</p>
    <p style="font-size:12px;line-height:25px;margin-top:6px">☏ &nbsp;1300-555-014<br>⎙ &nbsp;123-456-7890<br>✉ &nbsp;sales@velmoro.com.au</p>
  </div>
  <div class="fcol" style="left:990px;width:123px"><h5>Follow us</h5>
    <p style="font-size:12px;line-height:32px"><span class="social-mark"></span>Friendspace<br><span class="social-mark"></span>Chirper<br><span class="social-mark"></span>Circles<br><span class="social-mark"></span>Linkwork</p>
  </div>
</footer>
<div class="footer-bar">
  <span class="abs" style="left:87px;top:21px">Copyright © 2015 Velmoro Wireless. All Right Reserved. &nbsp;| &nbsp;Privacy Policy &nbsp;| &nbsp;Terms &amp; Conditions</span>
  <div class="abs" style="left:955px;top:8px;display:flex;align-items:center;gap:8px"><span style="width:26px;height:26px;border-radius:50%;background:#555;display:inline-block"></span><span style="font-family:'Exo 2',sans-serif;font-weight:700;font-size:28px;color:#666">Velmoro</span></div>
</div>

</body>
</html>
```